KRV Business Card - Courier/Transportation - Needs Double Sided Business Card

I am searching for business cards for my company. Currently I just need cards for the (3) founders.

We are a new courier/transporation company that specializes in the medical/pharmaceutical arena.

As you will see from our logo, our primary colors are green and black. We strive to have an efficient, streamlined service offering. I like traditional looks, but also want to showcase our young, modern feel. I would like our card to be double sided.

Target Market(s)

Pharmacies
Hospitals
Physcian Office
Labs

Industry/Entity Type

Business

```html
<!DOCTYPE html>
<html lang="en">
<head>
<meta charset="utf-8">
<title>KRV Courier – Business Card</title>
<link rel="stylesheet" href="https://fonts.googleapis.com/css2?family=PT+Sans:wght@400;700&display=swap">
<style>
  :root {
    --page: #ffffff;
    --card-dark-top: #221f1f;
    --card-dark-bottom: #434345;
    --card-light: #ffffff;
    --ink: #1c1c1c;
    --ink-soft: #333333;
    --brand-green: #1aaf4b;
    --green-text: #5cbd68;
    --on-dark: #f2f7fb;
    --card-shadow: rgba(0,0,0,0.35);
  }
  * { margin: 0; padding: 0; box-sizing: border-box; }
  html, body {
    width: 1200px; height: 1000px; overflow: hidden;
    background: var(--page);
    font-family: "PT Sans", sans-serif;
  }
  .canvas { position: relative; width: 1200px; height: 1000px; }

  .card {
    position: absolute; left: 305px; width: 587px; height: 340px;
    box-shadow: 0 1px 4px var(--card-shadow);
  }
  .card-front {
    top: 117px;
    background: linear-gradient(to bottom, var(--card-dark-top), var(--card-dark-bottom));
  }
  .card-back { top: 523px; background: var(--card-light); }

  .wordmark {
    position: absolute; display: flex; align-items: center; gap: 14px;
    font-weight: 700; letter-spacing: 1px; white-space: nowrap;
  }
  .wordmark-square { width: 30px; height: 30px; background: var(--brand-green); flex: none; }
  .card-front .wordmark {
    left: 0; right: 0; top: 140px; justify-content: center;
    font-size: 50px; color: var(--on-dark); line-height: 60px;
  }
  .card-back .wordmark {
    right: 40px; top: 52px; font-size: 40px; color: var(--ink-soft); line-height: 50px;
  }
  .card-back .wordmark-square { width: 24px; height: 24px; }

  .holder { position: absolute; left: 64px; top: 164px; color: var(--ink); }
  .holder-name { font-size: 29px; line-height: 34px; }
  .holder-title { font-size: 20px; line-height: 26px; }

  .contact { position: absolute; left: 24px; top: 256px; color: var(--ink); font-size: 25px; }
  .contact-row { display: flex; align-items: center; height: 31px; }
  .contact-row svg { width: 34px; height: 28px; margin-right: 6px; fill: var(--ink); }

  .address {
    position: absolute; right: 41px; top: 149px; text-align: right;
    color: var(--green-text); font-size: 21px; line-height: 28px;
  }
  .website {
    position: absolute; right: 31px; top: 291px;
    color: var(--ink); font-size: 20px;
  }
</style>
</head>
<body>
<main class="canvas">
  <section class="card card-front" aria-label="Card front">
    <div class="wordmark"><span class="wordmark-square"></span>KRV Courier</div>
  </section>

  <section class="card card-back" aria-label="Card back">
    <div class="wordmark"><span class="wordmark-square"></span>KRV Courier</div>

    <div class="address">
      KRV Courier<br>
      2450 Linden Ridge Dr,<br>
      Carmel Falls,<br>
      IN 46099
    </div>

    <div class="holder">
      <p class="holder-name">Mr.Hale</p>
      <p class="holder-title">Director</p>
    </div>

    <div class="contact">
      <p class="contact-row">
        <svg viewBox="0 0 34 28" aria-hidden="true">
          <path d="M8 2c2-1 4 0 5 2l2 5c1 2 0 3-1 4l-2 1c1 3 3 6 6 8l2-1c1-1 3-1 4 0l3 4c1 2 0 3-1 4-2 1-5 1-8-1C11 24 6 17 5 10 4 6 5 3 8 2z"/>
        </svg>
        000-00000000
      </p>
      <p class="contact-row">
        <svg viewBox="0 0 34 28" aria-hidden="true">
          <path d="M1 6h32v18H1z M3 8l14 10L31 8" fill="none" stroke="#1c1c1c" stroke-width="2"/>
          <path d="M1 6h32L17 17z"/>
        </svg>
        example@ mailbox.com
      </p>
    </div>

    <p class="website">www.KRVcourier.net</p>
  </section>
</main>
</body>
</html>
```